create clean, simple business card template

using the logo created now we need to create a simple, elegant business card design to suit

Industry/Entity Type

Business

Font styles to use
Other font styles liked:
• segoe ui

Requirements
Must have
• Front:
"Name:"
"Title:"
"Mobile:"
"email:"
and the logo

Back:
Logo
Nice to have
• Text in black but other graphics etc to match colours in logo as provided

```html
<!DOCTYPE html>
<html lang="en">
<head>
<meta charset="utf-8">
<title>Kestrel Homes – Business Cards</title>
<link rel="stylesheet" href="https://fonts.googleapis.com/css2?family=Open+Sans:ital,wght@0,400;0,600;0,700;1,400&display=swap">
<style>
  :root {
    --backdrop: #ece9e2;
    --card: #ffffff;
    --ink: #111111;
    --olive: #7b6c2e;
    --olive-text: #f1ecd8;
    --card-edge: #d8d4c8;
  }
  * { box-sizing: border-box; margin: 0; padding: 0; }
  html, body { width: 1200px; height: 782px; overflow: hidden; }
  body {
    background: var(--backdrop);
    font-family: "Open Sans", "Segoe UI", sans-serif;
    color: var(--ink);
    position: relative;
  }
  .card {
    position: absolute;
    width: 502px;
    height: 324px;
    background: var(--card);
    border: 1px solid var(--card-edge);
    overflow: hidden;
  }
  .card--front-white { left: 53px; top: 38px; }
  .card--front-band  { left: 53px; top: 395px; }
  .card--back        { left: 622px; top: 225px; }

  .holder { position: absolute; left: 46px; top: 70px; }
  .holder__name { font-size: 20px; font-weight: 700; line-height: 1.2; }
  .holder__title { font-size: 16px; font-style: italic; line-height: 1.2; }

  .brand {
    position: absolute;
    display: flex;
    align-items: center;
    gap: 8px;
    color: var(--olive);
    font-weight: 600;
    white-space: nowrap;
  }
  .brand__dot { border-radius: 50%; background: var(--olive); flex: none; }
  .card .brand--small { left: 276px; top: 48px; font-size: 22px; }
  .brand--small .brand__dot { width: 14px; height: 14px; }

  .address {
    position: absolute;
    left: 262px; top: 106px; width: 236px;
    text-align: center;
    font-size: 11.5px;
    line-height: 1.45;
  }

  .contact {
    position: absolute;
    left: 46px;
    font-size: 13.5px;
    line-height: 17.6px;
    display: grid;
    grid-template-columns: 75px auto;
  }
  .card--front-white .contact { top: 196px; }

  .band {
    position: absolute;
    left: 0; right: 0; top: 162px; bottom: 0;
    background: var(--olive);
  }
  .card--front-band .contact { top: 196px; color: var(--olive-text); }
  .card--front-band .contact dd { font-style: italic; }

  .card--back .brand--large {
    left: 50%; top: 50%;
    transform: translate(-50%, -50%);
    font-size: 44px;
    gap: 16px;
  }
  .brand--large .brand__dot { width: 30px; height: 30px; }
</style>
</head>
<body>

  <section class="card card--front-white" aria-label="Business card front, white">
    <div class="holder">
      <p class="holder__name">Daniel Marsh</p>
      <p class="holder__title">position</p>
    </div>
    <div class="brand brand--small"><span class="brand__dot"></span>Kestrel Homes</div>
    <p class="address">2218 Riverside, Oak lane 14.<br>Hungary</p>
    <dl class="contact">
      <dt>Telephone:</dt><dd>+(361) 2 3480 512 40</dd>
      <dt>Fax:</dt><dd>+(361) 2 3480 512 41</dd>
      <dt>Mobile:</dt><dd>+(361) 30 614 2875</dd>
      <dt>E-mail:</dt><dd>daniel.marsh@kestrelmail.com</dd>
    </dl>
  </section>

  <section class="card card--front-band" aria-label="Business card front, olive band">
    <div class="holder">
      <p class="holder__name">Daniel Marsh</p>
      <p class="holder__title">position</p>
    </div>
    <div class="brand brand--small"><span class="brand__dot"></span>Kestrel Homes</div>
    <p class="address">2218 Riverside, Oak lane 14.<br>Hungary</p>
    <div class="band"></div>
    <dl class="contact">
      <dt>Telephone:</dt><dd>+(361) 2 3480 512 40</dd>
      <dt>Fax:</dt><dd>+(361) 2 3480 512 41</dd>
      <dt>Mobile:</dt><dd>+(361) 30 614 2875</dd>
      <dt>E-mail:</dt><dd>daniel.marsh@kestrelmail.com</dd>
    </dl>
  </section>

  <section class="card card--back" aria-label="Business card back">
    <div class="brand brand--large"><span class="brand__dot"></span>Kestrel Homes</div>
  </section>

</body>
</html>
```